Darrow Consulting needs a quality & professional business card!

I am a recruitment and employment consultant from Brisbane, Australia and I had a fantastic logo organised by this community to I am hoping the business card will be the same.

I have attached the Darrow consulting logo that ideally would feature on the back of the business card. There are a number of logos for you to use as you see fit. I would like the colour cheme to match that of the Darrow Consulting logo. I also have a secondary company called Career Lantern Australia and I have included that logo as well. While it is an important part of the business I don't want this logo feature too predominantly as I am moving out of this space. This logo was created by myself and is of low quality. Feel free to use the icon and words however you want. The winning design will be smart, professional and eye-catching.

The information I am looking for in the business card is:
Name: Gavin Darrow
Position: Founder & Director
Phone: (07) 3519 6482
Mobile: 0431 586 207
Email: gavin@careerlantern.com.au

Target Market(s)

Recruiters, government, large companies

Contact Information for Business Card

Name: Gavin Darrow
Phone: (07) 3519 6482
Mobile: 0431 586 207
Web: www.careerlantern.com.au

Font styles to use
Serif
Sans Serif

Requirements
Must have
• Darrow Consulting Logo on reverse side
• Contact details on front side with smaller reference to Darrow Consulting logo and Career Lantern Australia logo

```html
<!DOCTYPE html>
<html lang="en">
<head>
<meta charset="UTF-8">
<title>Darrow Consulting – Business Card</title>
<link href="https://fonts.googleapis.com/css2?family=Open+Sans:wght@400;600;700&display=swap" rel="stylesheet">
<style>
  :root {
    --bg: #d9dadc;
    --card-dark: #1c1d1f;
    --card-dark-2: #3a3b3e;
    --paper: #ffffff;
    --paper-shade: #e6e7e8;
    --accent-blue: #0a8fd0;
    --ink: #222326;
    --text-light: #e9e9ea;
    --text-muted: #9a9b9e;
  }
  * { margin: 0; padding: 0; box-sizing: border-box; }
  html, body { width: 1200px; height: 900px; overflow: hidden; }
  body {
    background: var(--bg);
    font-family: "Open Sans", Arial, sans-serif;
    position: relative;
  }
  .card {
    position: absolute;
    left: 250px;
    width: 700px;
    height: 400px;
    border-radius: 20px;
    overflow: hidden;
    box-shadow: 0 14px 34px rgba(0,0,0,0.28);
  }
  .card-front { top: 40px; background: linear-gradient(160deg, var(--card-dark) 0%, var(--card-dark-2) 100%); }
  .card-back { top: 470px; background: linear-gradient(160deg, #2c2d30 0%, #48494c 100%); }

  .front-panel { position: absolute; inset: 0; }

  .contact-block { position: absolute; left: 40px; top: 120px; color: var(--text-light); }
  .person-name {
    font-size: 28px; font-weight: 600; color: var(--accent-blue);
    text-transform: uppercase; letter-spacing: 0.5px; line-height: 1.1;
  }
  .person-role { font-size: 16px; margin: 4px 0 22px; color: var(--text-light); }
  .contact-list { list-style: none; }
  .contact-item { display: flex; align-items: center; gap: 12px; font-size: 16px; line-height: 1.8; }
  .contact-icon { width: 14px; height: 14px; flex: none; }

  .wordmark-front {
    position: absolute; left: 430px; top: 140px;
    display: flex; align-items: center; gap: 14px;
  }
  .wordmark-square { width: 30px; height: 30px; background: var(--ink); }
  .wordmark-text {
    font-weight: 700; font-size: 28px; letter-spacing: 1px;
    color: var(--ink); text-transform: uppercase; line-height: 1.05;
  }

  .wordmark-back {
    position: absolute; left: 210px; top: 130px;
    display: flex; align-items: center; gap: 18px;
  }
  .wordmark-back .wordmark-square { width: 40px; height: 40px; background: #bfc0c2; }
  .wordmark-back .wordmark-text { color: #d4d5d7; font-size: 38px; }

  .secondary-brand {
    position: absolute; right: 40px; bottom: 34px;
  }
  .secondary-name { font-size: 20px; font-weight: 600; color: var(--text-light); }
</style>
</head>
<body>

<section class="card card-front" aria-label="Business card front">
  <svg class="front-panel" width="700" height="400" viewBox="0 0 700 400">
    <defs>
      <linearGradient id="paperFade" x1="0" y1="0" x2="1" y2="1">
        <stop offset="0" stop-color="var(--paper-shade)"/>
        <stop offset="0.5" stop-color="var(--paper)"/>
      </linearGradient>
    </defs>
    <path d="M390,0 Q270,200 410,400" fill="none" stroke="var(--accent-blue)" stroke-width="10"/>
    <path d="M402,0 Q284,200 422,400 L700,400 L700,0 Z" fill="url(#paperFade)"/>
  </svg>

  <div class="wordmark-front">
    <span class="wordmark-square"></span>
    <span class="wordmark-text">Darrow<br>Consulting</span>
  </div>

  <div class="contact-block">
    <h1 class="person-name">Gavin Darrow</h1>
    <p class="person-role">Founder &amp; Director</p>
    <ul class="contact-list">
      <li class="contact-item">
        <svg class="contact-icon" viewBox="0 0 14 14"><rect x="3" y="0.5" width="8" height="13" rx="1.5" fill="none" stroke="var(--accent-blue)" stroke-width="1.4"/><circle cx="7" cy="11" r="0.9" fill="var(--accent-blue)"/></svg>
        (07) 3519 6482
      </li>
      <li class="contact-item">
        <svg class="contact-icon" viewBox="0 0 14 14"><path d="M3 1 L5.5 1 L6.3 4 L4.8 5.2 Q6 8 8.8 9.2 L10 7.7 L13 8.5 L13 11 Q13 13 11 13 Q1 12 1 3 Q1 1 3 1 Z" fill="var(--accent-blue)"/></svg>
        0431 586 207
      </li>
      <li class="contact-item">
        <svg class="contact-icon" viewBox="0 0 14 14"><rect x="0.7" y="2.5" width="12.6" height="9" rx="1" fill="none" stroke="var(--accent-blue)" stroke-width="1.4"/><path d="M1 3 L7 8 L13 3" fill="none" stroke="var(--accent-blue)" stroke-width="1.4"/></svg>
        gavin@careerlantern.com.au
      </li>
    </ul>
  </div>
</section>

<section class="card card-back" aria-label="Business card back">
  <div class="wordmark-back">
    <span class="wordmark-square"></span>
    <span class="wordmark-text">Darrow<br>Consulting</span>
  </div>
  <div class="secondary-brand">
    <span class="secondary-name">Career Lantern Australia</span>
  </div>
</section>

</body>
</html>
```